Banner Designs for Trek Haven Ad Campaign

Quorvane is a security consulting and services company that offers a service called TrekHaven. TrekHaven helps our customers secure large events by providing rapidly deployable security and communications technologies in a Trek Haven vehicle, on a per event basis. We are looking for a designer to create a banner ad in three sizes for our campaign.
Target Market(s)
Our campaign is geared to the sports and entertainment industry, specifically large event venues and their security operation.
Industry/Entity Type
Security
Font styles to use
Other font styles liked:
- Raleway
Requirements
Must have
- Banner Objective
The visual and textual content of the banner should prompt the viewer to quickly identify the service offered and the information that is available to download.
Banner Design
Logo: TrekHaven logo
Call to Action Button in Red: Get Details (On Right or or Upper Right)
Title in Larger Font: Take Control of you Events
Subtitle in smaller Font: Your Force Multiplier - Trek Haven as a Service
Background: Photo of Trek Haven interior or exterior or photo of female operator.
Font: Raleway
Banner Sizes
1 - 1200x670 pixels
2 - 1510x196 pixels
3 - 1200x628 pixels
Nice to have
- Follow the look and feel of the samples provided.

```html
<!DOCTYPE html>
<html lang="en">
<head>
<meta charset="utf-8">
<title>Trek Haven Banner Set</title>
<link rel="stylesheet" href="https://fonts.googleapis.com/css2?family=Raleway:wght@400;500;700;800;900&display=swap">
<style>
  :root {
    --canvas-bg: #0a1d34;
    --panel-blue: #184878;
    --panel-blue-light: #1d5186;
    --band-grey: #8f9296;
    --photo-dark: #0c1118;
    --photo-mid: #3a3430;
    --photo-warm: #8a6e5c;
    --ribbon-red: #d90f0f;
    --text-white: #ffffff;
  }
  * { box-sizing: border-box; margin: 0; padding: 0; }
  html, body {
    width: 1051px;
    height: 1200px;
    overflow: hidden;
    background: var(--canvas-bg);
    font-family: "Raleway", sans-serif;
    color: var(--text-white);
  }
  .canvas { position: relative; width: 1051px; height: 1200px; }

  .banner { position: absolute; overflow: hidden; }
  .banner--large { left: 154px; top: 61px; width: 744px; height: 415px; }
  .banner--leaderboard { left: 58px; top: 539px; width: 936px; height: 121px; }
  .banner--medium { left: 154px; top: 725px; width: 744px; height: 389px; }

  .banner__photo {
    position: absolute; inset: 0;
    background:
      radial-gradient(ellipse 30% 55% at 72% 55%, var(--photo-warm) 0%, var(--photo-mid) 55%, transparent 100%),
      linear-gradient(90deg, var(--photo-dark) 0%, #1b2430 55%, #2a2622 100%);
  }
  .banner--leaderboard .banner__photo {
    background:
      radial-gradient(ellipse 9% 50% at 76% 55%, var(--photo-warm) 0%, var(--photo-mid) 60%, transparent 100%),
      linear-gradient(90deg, var(--photo-dark) 0%, #1a2433 60%, #141a22 100%);
  }
  .banner__shapes { position: absolute; inset: 0; width: 100%; height: 100%; }
  .shape-panel { fill: url(#panelGradient); }
  .shape-band { fill: var(--band-grey); }
  .shape-ribbon { fill: var(--ribbon-red); }

  .brand { position: absolute; text-align: right; }
  .brand__name { display: block; font-weight: 500; letter-spacing: -0.2px; line-height: 1; }
  .brand__by { display: block; font-weight: 500; line-height: 1; }
  .banner--large .brand, .banner--medium .brand { left: 60px; top: 70px; }
  .banner--large .brand__name, .banner--medium .brand__name { font-size: 31px; }
  .banner--large .brand__by, .banner--medium .brand__by { font-size: 14px; margin-top: 8px; }
  .banner--leaderboard .brand { left: 36px; top: 50px; }
  .banner--leaderboard .brand__name { font-size: 21px; }
  .banner--leaderboard .brand__by { font-size: 10px; margin-top: 4px; }

  .headline { position: absolute; font-weight: 900; text-transform: uppercase; letter-spacing: -0.5px; }
  .banner--large .headline, .banner--medium .headline { left: 38px; top: 172px; font-size: 45px; line-height: 55px; }
  .banner--leaderboard .headline { left: 255px; top: 18px; font-size: 30px; line-height: 36px; }

  .subline { position: absolute; font-weight: 500; }
  .banner--large .subline, .banner--medium .subline { left: 38px; top: 292px; font-size: 22px; line-height: 27px; width: 330px; }
  .banner--leaderboard .subline { left: 258px; top: 93px; font-size: 11.5px; }

  .cta {
    position: absolute; font-weight: 800; text-transform: uppercase;
    transform: translate(-50%, -50%) rotate(45deg);
    white-space: nowrap; letter-spacing: 0.3px;
  }
  .banner--large .cta, .banner--medium .cta { left: 690px; top: 50px; font-size: 20px; }
  .banner--leaderboard .cta { left: 896px; top: 40px; font-size: 14px; }
</style>
</head>
<body>
<main class="canvas">
  <svg width="0" height="0" aria-hidden="true" style="position:absolute">
    <defs>
      <linearGradient id="panelGradient" x1="0" y1="0" x2="1" y2="1">
        <stop offset="0" stop-color="#174677"/>
        <stop offset="1" stop-color="#1d4f82"/>
      </linearGradient>
    </defs>
  </svg>

  <section class="banner banner--large">
    <div class="banner__photo" role="img" aria-label="Photo of a female security operator wearing a headset in a dark control room"></div>
    <svg class="banner__shapes" viewBox="0 0 744 415" preserveAspectRatio="none" aria-hidden="true">
      <path class="shape-band" d="M0 0 H346 Q450 170 481 415 H0 Z"/>
      <path class="shape-panel" d="M0 0 H327 Q430 170 462 415 H0 Z"/>
      <path class="shape-ribbon" d="M614 0 H672 L744 72 V131 Z"/>
    </svg>
    <div class="brand"><span class="brand__name">TrekHaven</span><span class="brand__by">By Quorvane</span></div>
    <h1 class="headline">Take Control<br>of You Events</h1>
    <p class="subline">Your Force Multiplier - Trek Haven as a Service</p>
    <span class="cta">Get Details</span>
  </section>

  <section class="banner banner--leaderboard">
    <div class="banner__photo" role="img" aria-label="Photo of operators working at screens in a security control room"></div>
    <svg class="banner__shapes" viewBox="0 0 936 121" preserveAspectRatio="none" aria-hidden="true">
      <path class="shape-band" d="M0 0 H560 Q585 50 600 121 H0 Z"/>
      <path class="shape-panel" d="M0 0 H549 Q574 50 589 121 H0 Z"/>
      <path class="shape-ribbon" d="M824 0 H866 L936 70 V112 Z"/>
    </svg>
    <div class="brand"><span class="brand__name">TrekHaven</span><span class="brand__by">By Quorvane</span></div>
    <h2 class="headline">Take Control of<br>You Events</h2>
    <p class="subline">Your Force Multiplier - Trek Haven as a Service</p>
    <span class="cta">Get Details</span>
  </section>

  <section class="banner banner--medium">
    <div class="banner__photo" role="img" aria-label="Photo of a female security operator wearing a headset in a dark control room"></div>
    <svg class="banner__shapes" viewBox="0 0 744 389" preserveAspectRatio="none" aria-hidden="true">
      <path class="shape-band" d="M0 0 H346 Q450 160 481 389 H0 Z"/>
      <path class="shape-panel" d="M0 0 H327 Q430 160 462 389 H0 Z"/>
      <path class="shape-ribbon" d="M614 0 H672 L744 72 V131 Z"/>
    </svg>
    <div class="brand"><span class="brand__name">TrekHaven</span><span class="brand__by">By Quorvane</span></div>
    <h2 class="headline">Take Control<br>of You Events</h2>
    <p class="subline">Your Force Multiplier - Trek Haven as a Service</p>
    <span class="cta">Get Details</span>
  </section>
</main>
</body>
</html>
```